Flyer for Lawnmowing and gardening business

We are a lawn mowing and gardening business needing a flyer designed listing our services and business info.
The flyer should include all business information and contact details as below.

Lawn mowing
Gardening
Green waste removal
Pruning
Weeding
Vegetable Garden Creation

Phone number:0481657240

As well as the logo provided

Target Market(s)

Local people wanting someone to care for their garden.

Industry/Entity Type

Gardener

Font styles to use
Serif

Requirements
Must have
• Business Logo
• All business info and services provided. EG
• Lawn mowing
• Gardening
• Green waste removal
• Pruning
• Weeding
• Vegetable Garden Creation
• Phone number:0481657240
Nice to have
• Earthy tones, clean and simple flyer design

```html
<!DOCTYPE html>
<html lang="en">
<head>
<meta charset="utf-8">
<title>Maple Ridge Gardens – Services Flyer</title>
<link rel="stylesheet" href="https://fonts.googleapis.com/css2?family=Roboto+Condensed:wght@500;700&family=Roboto:wght@400&display=swap">
<style>
  :root {
    --bark: #3d2a1f;
    --ink: #3b2418;
    --leaf: #3a7a36;
    --sprout: #b8d98a;
    --paper: #ffffff;
    --backdrop: #d4d4d4;
  }
  * { box-sizing: border-box; margin: 0; padding: 0; }
  html, body { width: 1200px; height: 1200px; overflow: hidden; }
  body { background: var(--backdrop); position: relative; }

  .flyer {
    position: absolute; left: 222px; top: 62px;
    width: 756px; height: 1075px;
    background: var(--bark);
  }
  .panel {
    position: absolute; left: 26px; top: 28px;
    width: 704px; height: 1019px;
    background: var(--paper);
    border: 4px solid var(--sprout);
    border-radius: 46px;
    overflow: hidden;
  }
  .services-title {
    position: absolute; left: 41px; top: 54px;
    font: 700 62px/1 "Roboto Condensed", sans-serif;
    color: var(--leaf);
    white-space: nowrap;
  }
  .services-title .accent { color: var(--sprout); }

  .services-list {
    position: absolute; left: 41px; top: 136px;
    list-style: none;
  }
  .services-list li {
    display: flex; align-items: center;
    height: 48px;
    font: 500 38px/1 "Roboto Condensed", sans-serif;
    color: var(--ink);
    white-space: nowrap;
  }
  .services-list svg { width: 30px; height: 30px; margin-right: 18px; flex: none; }

  .divider {
    position: absolute; left: 24px; top: 470px;
    width: 652px; height: 2px; background: var(--ink);
  }

  .brand {
    position: absolute; left: 0; right: 0; top: 580px;
    display: flex; justify-content: center; align-items: center; gap: 16px;
  }
  .brand-dot {
    width: 34px; height: 34px; border-radius: 50%;
    background: var(--leaf); flex: none;
  }
  .brand-name {
    font: 700 50px/1 "Roboto Condensed", sans-serif;
    color: var(--ink);
    white-space: nowrap;
  }

  .contact-wave {
    position: absolute; left: 0; top: 805px;
    width: 704px; height: 214px;
  }
  .contact-lead {
    position: absolute; left: 40px; top: 898px;
    font: 400 29px/1 "Roboto", sans-serif;
    color: var(--paper);
  }
  .contact-phone {
    position: absolute; left: 38px; top: 933px;
    font: 400 55px/1 "Roboto", sans-serif;
    color: var(--paper);
  }
</style>
</head>
<body>
  <main class="flyer">
    <div class="panel">
      <h1 class="services-title">Services <span class="accent">Offered</span></h1>

      <ul class="services-list">
        <li><svg viewBox="0 0 30 30"><path d="M4 16 L12 24 L27 5" fill="none" stroke="#b8d98a" stroke-width="3.5" stroke-linecap="round" stroke-linejoin="round"/></svg>Lawn Mowing</li>
        <li><svg viewBox="0 0 30 30"><path d="M4 16 L12 24 L27 5" fill="none" stroke="#b8d98a" stroke-width="3.5" stroke-linecap="round" stroke-linejoin="round"/></svg>Gardening</li>
        <li><svg viewBox="0 0 30 30"><path d="M4 16 L12 24 L27 5" fill="none" stroke="#b8d98a" stroke-width="3.5" stroke-linecap="round" stroke-linejoin="round"/></svg>Green Waste Removal</li>
        <li><svg viewBox="0 0 30 30"><path d="M4 16 L12 24 L27 5" fill="none" stroke="#b8d98a" stroke-width="3.5" stroke-linecap="round" stroke-linejoin="round"/></svg>Pruning</li>
        <li><svg viewBox="0 0 30 30"><path d="M4 16 L12 24 L27 5" fill="none" stroke="#b8d98a" stroke-width="3.5" stroke-linecap="round" stroke-linejoin="round"/></svg>Weeding</li>
        <li><svg viewBox="0 0 30 30"><path d="M4 16 L12 24 L27 5" fill="none" stroke="#b8d98a" stroke-width="3.5" stroke-linecap="round" stroke-linejoin="round"/></svg>Vegetable Garden Creation</li>
      </ul>

      <div class="divider"></div>

      <div class="brand">
        <span class="brand-dot" aria-hidden="true"></span>
        <p class="brand-name">Maple Ridge Gardens</p>
      </div>

      <svg class="contact-wave" viewBox="0 0 704 214" preserveAspectRatio="none" aria-hidden="true">
        <path d="M0 22 C150 -18 330 40 480 80 S680 82 704 10 L704 214 L0 214 Z" fill="#b8d98a"/>
        <path d="M0 44 C150 8 330 62 480 102 S672 98 704 42 L704 214 L0 214 Z" fill="#3a7a36"/>
      </svg>
      <p class="contact-lead">Contact Us Today!</p>
      <p class="contact-phone">0481657240</p>
    </div>
  </main>
</body>
</html>
```